Pro-life non-profit needs a dynamic poster design for their Christmas Gala.

We need a poster design which plays off the name of the event, The Winter Lantern. The Winter Lantern, of course is the Baby Jesus. Our cause supports unborn children in Iowa. The gala will include a concert of popular Christmas music sung by top soloists backed by an orchestra. An original commissioned song, The Winter Lantern, will be premiered. Purple and gold colors immediately come to mind, but a designer should not feel constrained on colors. We need an editable design w/fonts. Photoshop w/layers or Illustrator files are good.

```html
<!DOCTYPE html>
<html lang="en">
<head>
<meta charset="utf-8">
<title>The Winter Lantern – A Pro-Life Christmas Gala</title>
<link rel="stylesheet" href="https://fonts.googleapis.com/css2?family=Montserrat:wght@400;500;600;700&family=Cormorant+Garamond:wght@500&family=Oswald:wght@500&display=swap">
<style>
  :root {
    --ink: #111111;
    --orange: #f7941d;
    --ring: #f6b974;
    --pink: #f6b8e6;
    --pink-deep: #ee94d8;
    --blush: #fde4f4;
    --white: #ffffff;
    --disc: #d9d6d9;
  }
  * { margin: 0; padding: 0; box-sizing: border-box; }
  html, body { width: 900px; height: 1200px; overflow: hidden; background: var(--white); }
  .poster {
    position: relative;
    width: 900px;
    height: 1200px;
    overflow: hidden;
    font-family: "Montserrat", sans-serif;
    color: var(--ink);
    background:
      radial-gradient(ellipse 46% 40% at 50% 58%, rgba(255,255,255,0.95) 0%, rgba(255,255,255,0.7) 55%, rgba(255,255,255,0) 100%),
      radial-gradient(circle at 12% 10%, var(--pink-deep) 0%, rgba(238,148,216,0) 35%),
      radial-gradient(circle at 90% 12%, var(--pink-deep) 0%, rgba(238,148,216,0) 32%),
      radial-gradient(circle at 8% 80%, var(--pink) 0%, rgba(246,184,230,0) 35%),
      radial-gradient(circle at 92% 78%, var(--pink) 0%, rgba(246,184,230,0) 35%),
      linear-gradient(180deg, var(--pink) 0%, var(--blush) 45%, var(--blush) 100%);
  }
  .frame { position: absolute; inset: 0; }
  .line { position: absolute; left: 0; width: 100%; text-align: center; white-space: nowrap; }

  .org-name { top: 48px; font-size: 19px; font-weight: 600; letter-spacing: 5px; }
  .presents { top: 86px; font-size: 13px; font-weight: 500; letter-spacing: 3px; }
  .banquet { top: 200px; font-size: 24px; font-weight: 600; letter-spacing: 5px; line-height: 31px; }

  .title-disc {
    position: absolute; left: 318px; top: 285px; width: 280px; height: 280px;
    border-radius: 50%; background: var(--disc);
  }
  .event-title {
    position: absolute; left: 0; top: 345px; width: 100%; text-align: center;
    font-weight: 600; color: var(--orange); line-height: 1.05; letter-spacing: 4px;
  }
  .event-title .title-the { display: block; font-size: 60px; }
  .event-title .title-main { display: block; font-size: 60px; }

  .gala { top: 620px; font-family: "Cormorant Garamond", serif; font-size: 24px; font-weight: 500; letter-spacing: 6px; }
  .speaker-label { top: 694px; font-size: 14px; font-weight: 600; letter-spacing: 4px; }
  .speaker { top: 722px; font-size: 35px; font-weight: 600; letter-spacing: 7px; }
  .date { top: 811px; font-size: 21px; font-weight: 600; letter-spacing: 4px; }
  .date .weekday { color: var(--orange); }
  .date sup { font-size: 11px; }
  .venue { top: 862px; font-size: 17px; font-weight: 600; letter-spacing: 4px; }

  .doors {
    position: absolute; left: 394px; top: 888px; width: 112px; height: 112px;
    border-radius: 50%; background: var(--orange);
    display: flex; flex-direction: column; align-items: center; justify-content: center;
  }
  .doors .doors-label { font-size: 11px; font-weight: 500; letter-spacing: 2px; }
  .doors .doors-time { font-size: 22px; font-weight: 600; letter-spacing: 3px; margin-top: 3px; }

  .pricing { top: 1008px; font-family: "Oswald", sans-serif; font-size: 22px; font-weight: 500; letter-spacing: 0.3px; }
  .pricing .dot { color: var(--orange); margin: 0 8px; }
  .seating { top: 1066px; font-size: 19px; font-weight: 600; letter-spacing: 5px; }
  .contact-web { top: 1093px; font-size: 15px; font-weight: 500; letter-spacing: 2.5px; }
  .contact-web .lead { color: var(--orange); }
  .contact-direct { top: 1114px; font-size: 15px; font-weight: 500; letter-spacing: 2.5px; }
  .contact-direct .dot { color: var(--orange); margin: 0 14px; }
</style>
</head>
<body>
<main class="poster">
  <svg class="frame" width="900" height="1200" viewBox="0 0 900 1200" aria-hidden="true">
    <ellipse cx="450" cy="590" rx="470" ry="575" fill="none" stroke="var(--ring)" stroke-width="3" opacity="0.85"/>
    <ellipse cx="445" cy="605" rx="455" ry="560" fill="none" stroke="var(--ring)" stroke-width="2" opacity="0.6"/>
  </svg>

  <p class="line org-name">HEARTLAND HOPE ALLIANCE</p>
  <p class="line presents">PRESENTS</p>
  <h2 class="line banquet">THE TENTH ANNUAL<br>FUNDRAISING BANQUET</h2>

  <div class="title-disc" aria-hidden="true"></div>
  <h1 class="event-title">
    <span class="title-the">THE</span>
    <span class="title-main">WINTER LANTERN</span>
  </h1>

  <p class="line gala">A&nbsp;&nbsp; PRO-LIFE&nbsp; CHRISTMAS GALA</p>
  <p class="line speaker-label">SPECIAL GUEST SPEAKER:</p>
  <p class="line speaker">BISHOP THOMAS ARDELL</p>
  <p class="line date"><span class="weekday">SATURDAY</span> NOVEMBER 21<sup>ST</sup>, 2020</p>
  <p class="line venue">MAPLE HALL CENTER, LINDEN PARK, IA</p>

  <div class="doors">
    <span class="doors-label">DOORS OPEN</span>
    <span class="doors-time">5:30PM</span>
  </div>

  <p class="line pricing">$60 PERSON<span class="dot">•</span>$500&nbsp; TABLE&nbsp; OF TEN COCKTAILS<span class="dot">•</span>DINNER<span class="dot">•</span>CHRISTMAS CONCERT</p>
  <p class="line seating">SEATING&nbsp; LIMITED&nbsp; • RESERVATIONS NEEDED</p>
  <p class="line contact-web"><span class="lead">Order tickets online</span>: www.HeartlandHope.org</p>
  <p class="line contact-direct">555-010-4 200<span class="dot">•</span>events@heartlandhope.org</p>
</main>
</body>
</html>
```